New Joomla Website for Marquee Hire Co

We need a web design for our new Marquee Hire Co here in New Zealand called Breezy Canopies.
We rather like the retro look, as it fit very well with the current trends in weddings that is a more of a retro look (and we had our logo designed to reflect that!). The 50's and 60's wedding styles are really making a comeback. We would like to communicate to that market effectively.

The Home page should have a slider image with space for a headline on it. It is a visual product we have (but we are selling that dream of a perfect wedding/party/event).

Our competition here have a really nice site that you could look at - www.plovanta.co.nz

The other pages would have space for a picture, and then a blurb under each element related to it.
We will have a FAQ, Gallery, Hire and Contact us pages - we will add them as we go along.

From a technical perspective, we are using Joomla 2.5 and upwards.

Any questions - let me know. I look forward seeing the designs!

Target Market(s)

Couples looking for a wedding marquee, birthday parties, Corporate events

Industry/Entity Type

Wedding

Requirements
Must have
• 1. Preferably done in Joomla. I will also look at Wordpress site.
2. It has to have a retro look and feel.
3. It has to use my brand new logo (included)

```html
<!DOCTYPE html>
<html lang="en">
<head>
<meta charset="utf-8">
<title>Breezy Canopies – Marquee Hire</title>
<link href="https://fonts.googleapis.com/css2?family=Righteous&family=Playball&family=PT+Sans:wght@400;700&family=Quattrocento+Sans:wght@400;700&display=swap" rel="stylesheet">
<style>
:root{
  --ribbon:#3f8fb8;
  --ribbon-dark:#2a6a8e;
  --ink:#3a3a3a;
  --teal:#1f6584;
  --teal-head:#2c6e8f;
  --page:#f6f6f6;
  --card:#fdf3ea;
  --card-line:#e4d9cc;
  --footer:#1b4f66;
  --footer-deep:#133b4d;
  --footer-text:#b9d3de;
  --bottom:#0f2f3d;
  --white:#ffffff;
}
*{box-sizing:border-box;margin:0;padding:0}
html,body{width:770px;height:1200px;overflow:hidden}
body{position:relative;background:var(--page);font-family:"PT Sans",Arial,sans-serif;color:var(--ink)}
.abs{position:absolute}

/* hero */
.hero{left:0;top:0;width:770px;height:433px;
  background:linear-gradient(180deg,#c79a68 0%,#b9895a 35%,#8a6a52 70%,#6a5a52 100%)}
.hero-photo{left:0;top:0;width:770px;height:433px;
  background:radial-gradient(ellipse at 50% 60%,rgba(255,255,255,.35) 0%,rgba(255,255,255,0) 45%),
  linear-gradient(90deg,rgba(40,30,40,.35) 0%,rgba(0,0,0,0) 20%,rgba(0,0,0,0) 80%,rgba(30,30,40,.4) 100%)}
.slider-arrow{top:206px;color:rgba(255,255,255,.8);font-size:40px;font-family:Arial,sans-serif}
.slider-arrow.prev{left:58px}
.slider-arrow.next{left:694px}
.hero-headline{left:0;width:770px;top:366px;text-align:center;font-family:"Righteous",sans-serif;
  font-size:18px;letter-spacing:1px;color:var(--white);text-decoration:underline;text-transform:uppercase;
  text-shadow:1px 1px 2px rgba(0,0,0,.6)}

/* nav ribbon */
.ribbon{left:80px;top:32px;width:612px;height:46px}
.nav a{position:absolute;top:46px;font-family:"Righteous",sans-serif;font-size:11px;color:var(--white);
  text-decoration:underline;text-transform:uppercase;letter-spacing:.5px}
.brand{left:322px;top:12px;width:126px;height:88px;display:flex;align-items:center;justify-content:center}
.brand-disc{position:absolute;left:18px;top:0;width:90px;height:90px;border-radius:50%;background:#e9dcc4;border:4px solid #6fb1d3}
.brand-name{position:relative;font-family:"Righteous",sans-serif;font-size:13px;color:#5a3a28;text-align:center;line-height:1.1;background:none}

/* welcome */
.welcome{left:111px;top:415px;width:548px;height:115px;background:var(--white);border-radius:4px;
  box-shadow:0 1px 4px rgba(0,0,0,.25)}
.welcome-photo{left:14px;top:8px;width:112px;height:100px;border-radius:4px;
  background:radial-gradient(circle at 50% 50%,#f3c03a 0%,#e9a534 30%,#f5f0ea 70%,#ffffff 100%)}
.welcome h1{position:absolute;left:150px;top:14px;font-family:"Playball",cursive;font-weight:400;font-size:21px;color:var(--teal-head)}
.welcome p{position:absolute;left:150px;top:46px;width:376px;font-size:11.2px;line-height:15px;color:var(--ink)}
.notch{width:28px;height:14px;background:var(--page);border-radius:0 0 14px 14px}

/* services */
.service{top:548px;width:176px;height:257px;background:var(--card);border:1px solid var(--card-line);border-radius:3px}
.service-photo{left:0;top:0;width:174px;height:112px}
.service h2{position:absolute;top:122px;width:100%;text-align:center;font-family:"Playball",cursive;font-weight:400;font-size:15px;color:var(--teal-head)}
.service p{position:absolute;top:148px;left:12px;width:150px;text-align:center;font-size:10.6px;line-height:13.6px}
.btn{display:inline-block;background:linear-gradient(#4f97c0,#23617f);color:var(--white);
  font-family:"PT Sans",sans-serif;font-weight:700;font-size:10px;border-radius:2px;text-align:center;
  box-shadow:0 1px 2px rgba(0,0,0,.3);text-decoration:none}
.service .btn{position:absolute;left:66px;top:224px;width:42px;height:18px;line-height:18px}
.zigzag{left:0;bottom:-6px;width:176px;height:6px}

/* testimonials */
.section-title{font-family:"Quattrocento Sans",sans-serif;font-size:12px;color:var(--teal-head)}
.testi-photo{left:112px;top:845px;width:127px;height:88px;border:3px solid var(--white);box-shadow:0 0 2px rgba(0,0,0,.3);
  background:linear-gradient(180deg,#3c5a2c 0%,#5e8a3c 55%,#7ba34a 100%)}
.quote{left:264px;top:847px;width:200px;font-size:10.2px;line-height:14px}
.quote-mark{font-family:Georgia,serif;color:var(--teal-head);font-size:16px;font-weight:700}
.quote cite{display:block;margin-top:4px;font-style:italic;font-weight:700;font-size:10px;color:var(--teal-head)}
.more-link{left:434px;top:916px;font-weight:700;font-size:10px;color:var(--teal);text-decoration:underline}
.quote-box{left:483px;top:826px;width:175px;height:107px;background:var(--card);border:1px solid var(--card-line);border-radius:3px;box-shadow:0 1px 2px rgba(0,0,0,.12)}
.quote-box h3{position:absolute;left:10px;top:6px;font-weight:400}
.quote-box hr{position:absolute;left:10px;top:22px;width:155px;border:0;border-top:1px dashed #c9b9a5}
.quote-box p{position:absolute;left:10px;top:28px;width:158px;font-size:10px;line-height:14px}
.quote-box .btn{position:absolute;left:44px;top:76px;width:84px;height:20px;line-height:20px}

/* footer */
.footer{left:0;top:961px;width:770px;height:175px;
  background:radial-gradient(ellipse at 50% 100%,#2a6d8a 0%,var(--footer) 45%,var(--footer-deep) 100%)}
.footer h4{position:absolute;top:25px;font-family:"Quattrocento Sans",sans-serif;font-weight:400;font-size:11.5px;color:#d7e8ef}
.footer .rule{position:absolute;top:44px;width:156px;border-top:1px dashed rgba(185,211,222,.35)}
.footer p,.footer li{font-size:9.4px;line-height:13.6px;color:var(--footer-text)}
.footer ul{list-style:none}
.footer .icon{display:inline-block;width:10px;height:10px;vertical-align:-1px;margin:0 6px 0 6px}
.bottom{left:0;top:1136px;width:770px;height:64px;background:var(--bottom)}
.bottom-nav{left:114px;top:20px;font-size:8px;color:#d0e0e8}
.bottom-nav span{color:#5f8799;margin:0 5px}
.copyright{left:114px;top:34px;font-size:8px;color:#6f97aa}
.follow{left:515px;top:22px;font-size:8.5px;color:#7fa3b4;display:flex;align-items:center;gap:6px}
.social{width:18px;height:18px;border-radius:50%;background:#2c7fa8}
</style>
</head>
<body>

<!-- hero slider -->
<section class="hero abs">
  <div class="hero-photo abs" role="img" aria-label="Slider photo: wedding couple exchanging vows at the altar with bridesmaid and groomsmen"></div>
  <span class="slider-arrow prev abs">‹</span>
  <span class="slider-arrow next abs">›</span>
  <div class="hero-headline abs">Some headline text goes here</div>
</section>

<!-- navigation ribbon -->
<svg class="ribbon abs" viewBox="0 0 612 46" aria-hidden="true">
  <polygon points="0,8 30,8 30,34 0,34 10,21" fill="var(--ribbon-dark)"/>
  <polygon points="612,8 582,8 582,34 612,34 602,21" fill="var(--ribbon-dark)"/>
  <rect x="22" y="4" width="568" height="30" rx="2" fill="var(--ribbon)"/>
  <rect x="22" y="4" width="568" height="3" fill="#6fb4d8"/>
  <line x1="22" y1="8" x2="590" y2="8" stroke="#8cc6e2" stroke-dasharray="3 2" stroke-width=".6"/>
  <line x1="22" y1="30" x2="590" y2="30" stroke="#8cc6e2" stroke-dasharray="3 2" stroke-width=".6"/>
</svg>
<nav class="nav">
  <a style="left:168px">Gallery</a>
  <a style="left:252px">Hire</a>
  <a style="left:504px">FAQ</a>
  <a style="left:564px">Contact us</a>
</nav>
<div class="brand abs">
  <span class="brand-disc"></span>
  <span class="brand-name">Breezy<br>Canopies</span>
</div>

<!-- welcome -->
<section class="welcome abs">
  <div class="welcome-photo abs" role="img" aria-label="Bouquet of yellow roses"></div>
  <h1>Welcome</h1>
  <p>Lorem ipsum dolor sit amet, consectetur adipisicing elit, sed do eiusmod tempor incididunt ut labore et dolore magna aliqua. Lorem ipsum dolor sit amet, consectetur adipisicing elit, sed do eiusmod tempor incididunt ut labore et dolore magna aliqua.</p>
</section>
<div class="notch abs" style="left:372px;top:415px"></div>
<div class="notch abs" style="left:372px;top:516px;border-radius:14px 14px 0 0"></div>

<!-- services -->
<article class="service abs" style="left:112px">
  <div class="service-photo abs" role="img" aria-label="White wedding canopy draped with flowers by the sea" style="background:linear-gradient(180deg,#6fa9d8 0%,#b9d4ea 50%,#f0eeea 75%,#8a9a70 100%)"></div>
  <h2>Wedding</h2>
  <p>Lorem ipsum dolor sit amet, consectetur adipisicing elit, sed do eiusmod tempor incididunt ut labore et dolore magna aliqua. Lorem ipsum dolor sit amet.</p>
  <a class="btn">More</a>
</article>
<article class="service abs" style="left:297px">
  <div class="service-photo abs" role="img" aria-label="Birthday cake with candles and glasses of red wine" style="background:radial-gradient(circle at 55% 55%,#f6e0e0 0%,#e4a0a0 30%,#8e2a24 70%,#4a1410 100%)"></div>
  <h2>Parties</h2>
  <p>Lorem ipsum dolor sit amet, consectetur adipisicing elit, sed do eiusmod tempor incididunt ut labore et dolore magna aliqua. Lorem ipsum dolor sit amet.</p>
  <a class="btn">More</a>
</article>
<article class="service abs" style="left:482px">
  <div class="service-photo abs" role="img" aria-label="Business team meeting around a table at a corporate event" style="background:linear-gradient(135deg,#5c8a40 0%,#8fb070 35%,#3a4a5a 65%,#d8d8dc 100%)"></div>
  <h2>Events</h2>
  <p>Lorem ipsum dolor sit amet, consectetur adipisicing elit, sed do eiusmod tempor incididunt ut labore et dolore magna aliqua. Lorem ipsum dolor sit amet.</p>
  <a class="btn">More</a>
</article>
<svg class="abs" style="left:112px;top:803px" width="547" height="8" aria-hidden="true">
  <defs><pattern id="zig" width="6" height="6" patternUnits="userSpaceOnUse"><polygon points="0,0 6,0 3,5" fill="var(--card)" stroke="var(--card-line)" stroke-width=".6"/></pattern></defs>
  <rect x="0" y="0" width="176" height="6" fill="url(#zig)"/>
  <rect x="185" y="0" width="176" height="6" fill="url(#zig)"/>
  <rect x="370" y="0" width="176" height="6" fill="url(#zig)"/>
</svg>

<!-- testimonials -->
<h3 class="section-title abs" style="left:113px;top:824px;font-weight:400">Testimonials</h3>
<div class="testi-photo abs" role="img" aria-label="Bride and groom in a garden"></div>
<blockquote class="quote abs">
  <span class="quote-mark">“</span> Lorem ipsum dolor sit amet, consectetur adipisicing elit, sed do eiusmod tempor incididunt ut labore et dolore magna aliqua. Lorem ipsum dolor sit amet, consectetur adipisicing elit. <span class="quote-mark">”</span>
  <cite>– M. Rowan, Kelby</cite>
</blockquote>
<a class="more-link abs">More...</a>

<aside class="quote-box abs">
  <h3 class="section-title">Get a Quote</h3>
  <hr>
  <p>Lorem ipsum dolor sit amet, eiusmod consectetur adipisicing elit, sed do eiusmod tempor incididunt hortugs.</p>
  <a class="btn">Quote Here</a>
</aside>

<!-- footer -->
<footer class="footer abs">
  <h4 style="left:113px">About Us</h4>
  <div class="rule" style="left:113px"></div>
  <p class="abs" style="left:113px;top:53px;width:158px">Lorem ipsum dolor sit amet, consectetur adipisicing elit, sed do eiusmod tempor incididunt ut labore et dolore magna aliqua. Lorem ipsum dolor sit amet, consectetur adipisicing elit, sed do eiusmod tempor incididunt ut labore et dolore. <b style="color:#e0eef4;margin-left:14px;text-decoration:underline">More...</b></p>

  <h4 style="left:301px">Contact Us</h4>
  <div class="rule" style="left:301px"></div>
  <ul class="abs" style="left:301px;top:53px">
    <li>42/C, Harbourview Crescent</li>
    <li>Tawa Lane, Kelby, New Zealand</li>
    <li><svg class="icon" viewBox="0 0 10 10"><path d="M2 1 L4 1 L4.6 3 L3.4 4 Q4.4 6 6 6.6 L7 5.4 L9 6 L9 8 Q5 9 1 4 Z" fill="var(--footer-text)"/></svg>800 - 555 0142/0187</li>
    <li><svg class="icon" viewBox="0 0 10 10"><path d="M2 1 L4 1 L4.6 3 L3.4 4 Q4.4 6 6 6.6 L7 5.4 L9 6 L9 8 Q5 9 1 4 Z" fill="var(--footer-text)"/></svg>800 - 555 0163</li>
    <li><svg class="icon" viewBox="0 0 10 10"><rect x="1" y="2.5" width="8" height="5.5" fill="none" stroke="var(--footer-text)"/><path d="M1 2.5 L5 5.5 L9 2.5" fill="none" stroke="var(--footer-text)"/></svg>hello@breezycanopies.nz</li>
    <li><svg class="icon" viewBox="0 0 10 10"><circle cx="5" cy="5" r="4" fill="var(--footer-text)"/></svg>breezy.canopies.chat</li>
  </ul>

  <h4 style="left:485px">Tweets</h4>
  <div class="rule" style="left:485px"></div>
  <div class="abs" style="left:485px;top:53px;width:160px">
    <p style="color:#e0eef4">Liam Tarrow, 12-June-2013</p>
    <p>Lorem ipsum dolor sit amet, onsectetur adipisicing elit amet.</p>
    <div style="border-top:1px dashed rgba(185,211,222,.35);margin:8px 0 6px"></div>
    <p style="color:#e0eef4">Liam Tarrow, 12-June-2013</p>
    <p>Lorem ipsum dolor sit amet, onsectetur adipisicing elit amet.</p>
  </div>
</footer>

<div class="bottom abs">
  <div class="bottom-nav abs">Home<span>|</span>Gallery<span>|</span>Hire<span>|</span>Faq<span>|</span>Contact us</div>
  <div class="copyright abs">Copyright©2013, Privacy Policy</div>
  <div class="follow abs">Follow Us :
    <span class="social"></span><span class="social"></span><span class="social"></span>
  </div>
</div>

</body>
</html>
```